Velk Method Body Wash & Shampoo

Label design for an Activated charcoal body wash and shampoo for first responders after fires. Product removes soot and smoke smell. Deep cleansing. Red and black tones in label. Product is deep black and bottle transparent. Label is wrapped around bottle and can be with transparent or coloured background. Bottle diameter is 19cm and height is 17cm.

Target Market(s)

Product will be used by Firefighters, first responders, outdoor/nature active and grill enthusiasts.

Industry/Entity Type

Health and hygiene

Colors
EB3D1F
EC4F4E
F09395
F8D3D4
FCEDEE

Requirements
Must have
• Serious design. Design that fits for 250 and 500ml bottles. Place for ingredients and contact info at the back of the bottle..
Nice to have
• Attractive clean design, attached logo. Logo can be on front or back. "medical" or health associations would be good.
Should not have
• Multi color, pictures. Playfulness.

```html
<!DOCTYPE html>
<html lang="en">
<head>
<meta charset="utf-8">
<title>Velk Method Body Wash &amp; Shampoo – Label</title>
<link href="https://fonts.googleapis.com/css2?family=Open+Sans:wght@300;400;700;800&display=swap" rel="stylesheet">
<style>
  :root {
    --stage: #e2e2e2;
    --ink-black: #0b0b0b;
    --ink-dark: #1c1c1e;
    --mid-grey: #6d6d72;
    --soft-white: #f4f4f6;
    --brand-red: #d3262c;
    --band-red: #cc1f24;
    --band-red-text: #8e1418;
    --strip-grey: #59595c;
    --strip-white: #f2f2f2;
    --caption: #3a3a3c;
  }
  * { box-sizing: border-box; margin: 0; padding: 0; }
  html, body {
    width: 1200px; height: 900px; overflow: hidden;
    background: var(--stage);
    font-family: "Open Sans", Arial, sans-serif;
  }
  .canvas {
    position: relative; width: 1200px; height: 900px;
  }
  .label {
    position: absolute; left: 445px; top: 30px;
    width: 310px; height: 840px;
    border-radius: 6px;
    overflow: hidden;
    background: linear-gradient(to bottom,
      var(--ink-black) 0%,
      var(--ink-black) 32%,
      #2a2a2d 48%,
      var(--mid-grey) 66%,
      #b9b9bd 84%,
      var(--soft-white) 100%);
  }
  .charcoal-scene {
    position: absolute; left: 0; top: 330px; width: 310px; height: 320px;
    background:
      radial-gradient(ellipse 60% 30% at 75% 30%, rgba(255,255,255,0.18), transparent 70%),
      radial-gradient(ellipse 40% 25% at 15% 62%, rgba(20,20,20,0.55), transparent 75%),
      radial-gradient(ellipse 50% 20% at 80% 70%, rgba(10,10,10,0.6), transparent 75%),
      linear-gradient(160deg, transparent 45%, rgba(255,255,255,0.22) 55%, transparent 65%);
  }
  .brand {
    position: absolute; left: 0; top: 170px; width: 100%;
    text-align: center;
    color: var(--brand-red);
    font-weight: 800; font-size: 40px; letter-spacing: 0.5px;
  }
  .product-type {
    position: absolute; left: 0; top: 290px; width: 100%;
    text-align: center;
    color: var(--brand-red);
    font-weight: 700; font-size: 17px; letter-spacing: -0.2px;
  }
  .variant-box {
    position: absolute; left: 55px; top: 488px; width: 198px;
    box-shadow: 0 2px 6px rgba(0,0,0,0.35);
  }
  .variant-name {
    background: var(--band-red);
    color: var(--band-red-text);
    font-weight: 300; font-size: 21px; letter-spacing: 0.5px;
    text-align: center; height: 42px; line-height: 42px;
  }
  .variant-claim {
    background: var(--strip-grey);
    color: #f0f0f0;
    font-size: 12px; font-weight: 400;
    text-align: center; height: 30px; line-height: 30px;
  }
  .variant-tag {
    background: var(--strip-white);
    color: var(--ink-dark);
    font-size: 8.5px; font-weight: 700;
    height: 22px; line-height: 22px;
    padding-left: 54px;
  }
  .approval {
    position: absolute; left: 0; top: 676px; width: 100%; text-align: center;
  }
  .approval-caption {
    color: var(--caption); font-size: 7px; font-weight: 700; letter-spacing: 0.3px;
  }
  .approval-badge {
    display: block; margin: 8px auto 0;
  }
  .volume {
    position: absolute; left: 0; top: 764px; width: 100%; text-align: center;
    color: var(--caption); font-size: 13px; font-weight: 400;
  }
</style>
</head>
<body>
<div class="canvas">
  <section class="label">
    <div class="charcoal-scene" role="img" aria-label="Activated charcoal powder, a charcoal stick and soap bubbles with a light swoosh"></div>

    <div class="brand">Velk Method</div>
    <div class="product-type">BODY WASH &amp; SHAMPOO</div>

    <div class="variant-box">
      <div class="variant-name">CHARCOAL</div>
      <div class="variant-claim">Removes soot and smoke smell</div>
      <div class="variant-tag">DEEP CLEANSING</div>
    </div>

    <div class="approval">
      <div class="approval-caption">APPROVED BY:</div>
      <svg class="approval-badge" width="46" height="46" viewBox="0 0 46 46" aria-hidden="true">
        <circle cx="23" cy="23" r="21" fill="#3a3a3c"/>
      </svg>
    </div>

    <div class="volume">250ML</div>
  </section>
</div>
</body>
</html>
```